Business card design for web travel company

Hi
we'd like to receive some proposal for a business card design.
Stayvano is a private travel club, dedicated to all travel lovers, with unique offers for exclusive destinations all around the world. At Stayvano you can find a wide range of offers for resorts, boutique hotels and travel packages at the best guaranteed price available on the market. The convenience of the offer is guaranteed by a private sales model: offers are available for a limited time only and they are personally chosen by Stayvano's qualified team of travel experts.
We offer only exclusive hotels with discounted prices but we are not an outlet or a discount supermarket: the design should reflect our connection with luxury, exclusivity using the same style of our website www.stayvano-example.com.
We want to make sure that when we'll present ourself to our business partner they will feel immediately which is our brand positioning giving them also a sense of an affordable and reliable partner.
In attachment you can also find our brand guidelines (please note that we are NOT USING ANY MORE THE TAG LINE "Five star outlet" mentioned in it).
The info to be inserted are:
Name Surname
Job Title
Tel
Mobile (when needed)
Email
Stayvano S.r.l.
Via Bruno Lesta 27
20131 Milano

```html
<!DOCTYPE html>
<html lang="en">
<head>
<meta charset="utf-8">
<title>Stayvano Business Card</title>
<link rel="stylesheet" href="https://fonts.googleapis.com/css2?family=Arimo:wght@400;700&family=Quicksand:wght@400&display=swap">
<style>
  :root {
    --gold: #d1b766;
    --band: #2b2b2b;
    --band-edge: #1f1f1f;
    --paper: #f4f4f4;
    --ink: #1e1e1e;
    --white: #ffffff;
    --frame: #3a3a3a;
  }
  * { box-sizing: border-box; margin: 0; padding: 0; }
  html, body { width: 1078px; height: 1200px; overflow: hidden; background: var(--white); }
  body {
    position: relative;
    font-family: "Arimo", Arial, sans-serif;
    border: 2px solid var(--frame);
  }
  .card {
    position: absolute;
    left: 130px;
    width: 777px;
    height: 473px;
    box-shadow: 10px 10px 14px rgba(0,0,0,0.16);
    overflow: hidden;
  }
  .card--front { top: 71px; background: var(--gold); }
  .card--back { top: 613px; background: var(--paper); }

  .band {
    position: absolute;
    left: 0;
    background: var(--band);
    border-top: 1px solid var(--band-edge);
    border-bottom: 1px solid var(--band-edge);
  }
  .band__rule {
    position: absolute;
    height: 4px;
    background: linear-gradient(90deg, rgba(255,255,255,0.15) 0%, #ffffff 20%, #9a9a9a 45%, #ffffff 70%, rgba(255,255,255,0.15) 100%);
  }

  .card--front .band { top: 148px; width: 100%; height: 178px; }
  .card--front .band__rule { left: 19px; right: 19px; }
  .card--front .band__rule--top { top: 24px; }
  .card--front .band__rule--bottom { top: 160px; }
  .brand-name {
    font-family: "Arimo", Arial, sans-serif;
    font-weight: 400;
    color: var(--white);
  }
  .card--front .brand-name {
    position: absolute;
    top: 0; left: 0; right: 0; bottom: 0;
    display: flex; align-items: center; justify-content: center;
    font-size: 64px;
    letter-spacing: 1px;
  }

  .side {
    position: absolute;
    top: 0; left: 0;
    width: 310px; height: 100%;
    background: var(--gold);
  }
  .card--back .band { top: 148px; width: 310px; height: 178px; }
  .card--back .band__rule { left: 12px; right: 2px; }
  .card--back .band__rule--top { top: 11px; }
  .card--back .band__rule--bottom { top: 160px; }
  .person { position: absolute; left: 45px; top: 48px; }
  .person__name { color: var(--white); font-weight: 700; font-size: 33px; line-height: 1.1; }
  .person__title { color: var(--gold); font-size: 17px; margin-top: 16px; text-transform: uppercase; }

  .card--back .brand-name {
    position: absolute;
    right: 43px; top: 54px;
    color: var(--ink);
    font-size: 40px;
    letter-spacing: 0.5px;
  }
  .contact {
    position: absolute;
    left: 429px; top: 142px;
    font-size: 22px;
    line-height: 31px;
    color: var(--ink);
  }
  .contact__company { font-weight: 700; }
  .contact__label { color: var(--gold); margin-right: 6px; }
  .contact__value { font-size: 20px; }
</style>
</head>
<body>
  <section class="card card--front">
    <div class="band">
      <span class="band__rule band__rule--top"></span>
      <span class="brand-name">Stayvano</span>
      <span class="band__rule band__rule--bottom"></span>
    </div>
  </section>

  <section class="card card--back">
    <div class="side">
      <div class="band">
        <span class="band__rule band__rule--top"></span>
        <div class="person">
          <p class="person__name">Name Surname</p>
          <p class="person__title">Job Title</p>
        </div>
        <span class="band__rule band__rule--bottom"></span>
      </div>
    </div>
    <span class="brand-name">Stayvano</span>
    <address class="contact" style="font-style:normal">
      <p class="contact__company">Stayvano S.r.l.</p>
      <p>Via Bruno Lesta 27</p>
      <p>20131 Milano</p>
      <p><span class="contact__label">Tel</span><span class="contact__value">xxxxxxxxxxxxxx</span></p>
      <p><span class="contact__label">Mobile</span> <span class="contact__value">xxxxxxxxxxxxxx</span></p>
      <p><span class="contact__label">Email</span> <span class="contact__value">xxxxxxxxxxxxxx</span></p>
    </address>
  </section>
</body>
</html>
```